Tiny Sprout nursery
Learning throu fun & activities
Bright & Fun-filled
Rashid Al Fahim (K-07)
tinysprout_ns@quellmail.com
www.tinysprout-ns.com
P.O.Box 51862
To be as points
Logo vector file

```html
<!DOCTYPE html>
<html lang="en">
<head>
<meta charset="utf-8">
<title>Tiny Sprout nursery – business card options</title>
<link href="https://fonts.googleapis.com/css2?family=Comic+Neue:wght@700&display=swap" rel="stylesheet">
<style>
  :root {
    --page: #ffffff;
    --sunny: #ffe81a;
    --paper: #ffffff;
    --coral: #ef4a24;
    --ink: #1c1c1c;
    --ink-blue: #1b3f8f;
    --tag-blue: #1d5fc4;
    --brand-pink: #e4157f;
    --cream: #fff6a0;
    --swoosh: #b9b9b9;
    --rim-rainbow: linear-gradient(135deg, #1fa4e8 0%, #22b573 22%, #ffd200 45%, #f7931e 62%, #ec1c7c 82%, #8e3fbf 100%);
    --rim-sunset: linear-gradient(135deg, #8dc63f 0%, #00b3d9 25%, #ffd200 50%, #f7931e 75%, #ff3b8d 100%);
  }
  html, body {
    margin: 0;
    padding: 0;
    width: 1200px;
    height: 845px;
    overflow: hidden;
    background: var(--page);
  }
  .sheet {
    position: relative;
    width: 1200px;
    height: 845px;
  }
  .card {
    position: absolute;
    width: 440px;
    height: 258px;
    padding: 7px;
    box-sizing: border-box;
    border-radius: 16px;
    background: var(--rim-rainbow);
  }
  .card--one   { left: 136px; top: 132px; }
  .card--two   { left: 628px; top: 132px; }
  .card--three { left: 136px; top: 451px; }
  .card--four  { left: 628px; top: 451px; background: var(--rim-sunset); }

  .card__face {
    position: relative;
    width: 100%;
    height: 100%;
    border-radius: 11px;
    background: var(--paper);
    font-family: "Comic Neue", "Comic Sans MS", cursive;
    font-weight: 700;
    color: var(--ink);
  }
  .card--one  .card__face { background: var(--sunny); }
  .card--four .card__face { background: var(--coral); color: #ffffff; }

  .brand {
    position: absolute;
    left: 92px;
    top: 20px;
    width: 260px;
    height: 110px;
  }
  .brand__baby {
    position: absolute;
    left: 0;
    top: 8px;
    width: 62px;
    height: 78px;
    border-radius: 30px 30px 18px 18px;
    background: linear-gradient(180deg, #f9d2b0 0%, #f6b98e 55%, #e4157f 56%, #c8106d 100%);
  }
  .brand__name {
    position: absolute;
    left: 72px;
    top: 14px;
    width: 170px;
    font-size: 27px;
    line-height: 30px;
    color: var(--brand-pink);
  }
  .card--four .brand__name { color: var(--cream); }
  .brand__swoosh {
    position: absolute;
    left: 4px;
    top: 86px;
    width: 250px;
    height: 10px;
  }
  .brand__tagline {
    position: absolute;
    left: 0;
    top: 94px;
    width: 260px;
    text-align: center;
    font-size: 14px;
    color: var(--tag-blue);
  }
  .card--four .brand__tagline { color: #ffffff; }

  .contact {
    position: absolute;
    top: 163px;
    font-size: 13px;
    line-height: 15px;
    margin: 0;
  }
  .contact--left  { left: 16px; }
  .contact--right { left: 272px; }
  .contact span { display: block; white-space: nowrap; }
  .contact b { color: var(--ink-blue); }
  .card--four .contact b { color: var(--cream); }
</style>
</head>
<body>
<main class="sheet">

  <section class="card card--one">
    <div class="card__face">
      <div class="brand">
        <div class="brand__baby" role="img" aria-label="Illustration of a smiling baby mascot"></div>
        <div class="brand__name">Tiny Sprout nursery</div>
        <svg class="brand__swoosh" viewBox="0 0 250 10" aria-hidden="true"><path d="M2 8 Q125 -2 248 8" fill="none" stroke="var(--swoosh)" stroke-width="3"/></svg>
        <div class="brand__tagline">Learning Through Fun &amp; Activities</div>
      </div>
      <p class="contact contact--left">
        <span>Address:</span>
        <span>Rashid Al Fahim (K-07)</span>
        <span>Email: <b>tinysprout_ns@quellmail.com</b></span>
        <span>Web: <b>www.tinysprout-ns.com</b></span>
      </p>
      <p class="contact contact--right">
        <span>Phone: <b>02-4870316</b></span>
        <span>Cell: <b>055-712-0948</b></span>
        <span>Fax: <b>02-4870319</b></span>
        <span>P.O.Box 51862</span>
      </p>
    </div>
  </section>

  <section class="card card--two">
    <div class="card__face">
      <div class="brand">
        <div class="brand__baby" role="img" aria-label="Illustration of a smiling baby mascot"></div>
        <div class="brand__name">Tiny Sprout nursery</div>
        <svg class="brand__swoosh" viewBox="0 0 250 10" aria-hidden="true"><path d="M2 8 Q125 -2 248 8" fill="none" stroke="var(--swoosh)" stroke-width="3"/></svg>
        <div class="brand__tagline">Learning Through Fun &amp; Activities</div>
      </div>
      <p class="contact contact--left">
        <span>Address:</span>
        <span>Rashid Al Fahim (K-07)</span>
        <span>Email: <b>tinysprout_ns@quellmail.com</b></span>
        <span>Web: <b>www.tinysprout-ns.com</b></span>
      </p>
      <p class="contact contact--right">
        <span>Phone: <b>02-4870316</b></span>
        <span>Cell: <b>055-712-0948</b></span>
        <span>Fax: <b>02-4870319</b></span>
        <span>P.O.Box 51862</span>
      </p>
    </div>
  </section>

  <section class="card card--three">
    <div class="card__face">
      <div class="brand">
        <div class="brand__baby" role="img" aria-label="Illustration of a smiling baby mascot"></div>
        <div class="brand__name">Tiny Sprout nursery</div>
        <svg class="brand__swoosh" viewBox="0 0 250 10" aria-hidden="true"><path d="M2 8 Q125 -2 248 8" fill="none" stroke="var(--swoosh)" stroke-width="3"/></svg>
        <div class="brand__tagline">Learning Through Fun &amp; Activities</div>
      </div>
      <p class="contact contact--left">
        <span>Address:</span>
        <span>Rashid Al Fahim (K-07)</span>
        <span>Email: <b>tinysprout_ns@quellmail.com</b></span>
        <span>Web: <b>www.tinysprout-ns.com</b></span>
      </p>
      <p class="contact contact--right">
        <span>Phone: <b>02-4870316</b></span>
        <span>Cell: <b>055-712-0948</b></span>
        <span>Fax: <b>02-4870319</b></span>
        <span>P.O.Box 51862</span>
      </p>
    </div>
  </section>

  <section class="card card--four">
    <div class="card__face">
      <div class="brand">
        <div class="brand__baby" role="img" aria-label="Illustration of a smiling baby mascot"></div>
        <div class="brand__name">Tiny Sprout nursery</div>
        <svg class="brand__swoosh" viewBox="0 0 250 10" aria-hidden="true"><path d="M2 8 Q125 -2 248 8" fill="none" stroke="#ffffff" stroke-width="3"/></svg>
        <div class="brand__tagline">Learning Through Fun &amp; Activities</div>
      </div>
      <p class="contact contact--left">
        <span>Address:</span>
        <span><b>Rashid Al Fahim (K-07)</b></span>
        <span>Email: <b>tinysprout_ns@quellmail.com</b></span>
        <span>Web: <b>www.tinysprout-ns.com</b></span>
      </p>
      <p class="contact contact--right">
        <span>Phone: <b>02-4870316</b></span>
        <span>Cell: <b>055-712-0948</b></span>
        <span>Fax: <b>02-4870319</b></span>
        <span>P.O.Box 51862</span>
      </p>
    </div>
  </section>

</main>
</body>
</html>
```